Manufacturing company needs new business card.

I need a unique Business Card that will truly stand out. Nothing too busy. Simple is good, right? Not looking for a standard design either. No cookie cutter layout. I am just looking for something interesting and a bit different. Does't have to completely off the wall crazy, just not your run of the mill business card. Clean and modern with a touch of industrial.

Target Market(s)

Air conditioning industry, Architects, builders.

Industry/Entity Type

Business

Contact Information for Business Card

Details to be included on card are:

Peter Vance
Managing Director

T: 1300 847 519
M: 0428 593 174
W: www.brenvaleworks.com.au
E: peter.vance@brenvaleworks.com.au
A: 58 Harwick Lane, Sydney NSW 2000

Font styles to use
Sans Serif

Colors
0355a3
848484
fbfbfb

Requirements
Must have
• Card design must be landscape.

```html
<!DOCTYPE html>
<html lang="en">
<head>
<meta charset="utf-8">
<title>Brenvale Works – Business Card</title>
<link href="https://fonts.googleapis.com/css2?family=Source+Sans+3:wght@400;600;700&display=swap" rel="stylesheet">
<style>
  :root {
    --brand-blue: #1f4fa3;
    --steel-grey: #848484;
    --paper: #fbfbfb;
    --ink: #4a4a4a;
    --backdrop: #54463a;
  }
  * { margin: 0; padding: 0; box-sizing: border-box; }
  html, body {
    width: 1200px; height: 987px; overflow: hidden;
    background: var(--backdrop);
    font-family: "Source Sans 3", sans-serif;
  }
  .card {
    position: absolute;
    left: 292px;
    width: 616px; height: 352px;
    background: var(--paper);
    box-shadow: 0 2px 4px rgba(0,0,0,0.35);
    overflow: hidden;
  }
  .card--front { top: 130px; }
  .card--back { top: 505px; }

  .brand {
    position: absolute;
    display: flex; align-items: center; gap: 10px;
    color: var(--brand-blue);
    font-weight: 600;
    white-space: nowrap;
  }
  .brand__square { background: var(--steel-grey); display: block; }
  .card--front .brand { left: 41px; top: 46px; font-size: 28px; }
  .card--front .brand__square { width: 18px; height: 18px; }

  .bands { position: absolute; left: 0; top: 0; }

  .holder { position: absolute; left: 41px; top: 245px; color: #fff; }
  .holder__name { font-size: 22px; font-weight: 600; line-height: 1.2; }
  .holder__role { font-size: 16px; line-height: 1.3; }

  .contact {
    position: absolute; right: 29px; top: 185px;
    color: #fff; font-size: 15.5px; text-align: right;
    list-style: none;
  }
  .contact li { height: 23.5px; line-height: 23.5px; display: flex; justify-content: flex-end; align-items: center; gap: 6px; }
  .contact .address { padding-right: 0; }
  .contact .address + .address { margin-bottom: 5px; }
  .contact svg { width: 14px; height: 14px; flex: none; }

  .card--back .brand {
    left: 0; right: 0; top: 150px; justify-content: center;
    font-size: 44px;
  }
  .card--back .brand__square { width: 30px; height: 30px; }
  .back-web {
    position: absolute; left: 0; right: 0; top: 302px;
    text-align: center; color: var(--ink);
    font-size: 16px; letter-spacing: 2px;
  }
</style>
</head>
<body>

<section class="card card--front">
  <div class="brand"><span class="brand__square"></span>Brenvale Works</div>

  <svg class="bands" width="616" height="352" viewBox="0 0 616 352">
    <polygon fill="#848484" points="0,192 320,192 303,210 0,210"/>
    <polygon fill="#1f4fa3" points="358,159 616,159 616,352 0,352 0,212 307,212"/>
  </svg>

  <div class="holder">
    <div class="holder__name">Peter Vance</div>
    <div class="holder__role">Managing Director</div>
  </div>

  <ul class="contact">
    <li class="address">58 Harwick Lane</li>
    <li class="address">Sydney NSW 2000</li>
    <li>1300 847 519
      <svg viewBox="0 0 16 16"><path fill="#fff" d="M3.6 1.5l2.3 2.6-1.3 1.9c.9 2 2.5 3.6 4.5 4.6l1.9-1.3 2.6 2.3-1.2 2.3C6.6 14.2 1.8 9.4 1.3 2.7z"/></svg>
    </li>
    <li>0428 593 174
      <svg viewBox="0 0 16 16"><rect x="4" y="1" width="8" height="14" rx="1.5" fill="none" stroke="#fff" stroke-width="1.6"/><rect x="7" y="12" width="2" height="1.2" fill="#fff"/></svg>
    </li>
    <li>peter.vance@brenvaleworks.com.au
      <svg viewBox="0 0 16 16"><rect x="1" y="3.5" width="14" height="9" fill="#fff"/><path d="M1.5 4l6.5 5 6.5-5" fill="none" stroke="#1f4fa3" stroke-width="1.2"/></svg>
    </li>
    <li>www.brenvaleworks.com.au
      <svg viewBox="0 0 16 16"><circle cx="8" cy="8" r="7" fill="#fff"/><path d="M1 8h14M8 1c-3 3.5-3 10.5 0 14M8 1c3 3.5 3 10.5 0 14" fill="none" stroke="#1f4fa3" stroke-width="1"/></svg>
    </li>
  </ul>
</section>

<section class="card card--back">
  <div class="brand"><span class="brand__square"></span>Brenvale Works</div>
  <p class="back-web">www.brenvaleworks.com.au</p>
</section>

</body>
</html>
```